New Website for Asia Travel Agency

Lantern Route Website

We want a redesign for our current website, www.lanternroute.com. We want you to get creative with our brand and present our company in a unique, creative and compelling way, that communicates our exotic destinations and tours, the local and authentic character of our travel consultants and the trustworthy and professional nature of our company.

Who is this company?

Lantern Route is an online tour operator specializing in providing tailor-made tours to eight destinations in Asia; Vietnam, Thailand, Laos, Cambodia, Indonesia, Myanmar, Japan and China. They were launched in mid February 2012 with headquarters in Bangkok, Thailand, and staffed by locals and expats with many years of experience in the travel industry, and who are committed to sharing their deep knowledge of, and passion for the region.

Local knowledge

Our consultants at Lantern Route are all locals – they know their destinations inside-out and draw upon invaluable first-hand experience and information when planning your tour. They have insights into local culture and tradition, they know the best places to visit, the most worthwhile experiences to have and, most importantly, they have the knowledge to create exactly the holiday you desire.

All hotels and activities featured in a Lantern Route tour are regularly inspected by our consultants to ensure the highest quality standards are met and that all information is correct and up to date.

Unforgettable Travel Experiences

Whether it's a cultural exploration or a beach holiday you're after – or a mix of both – Lantern Route has an itinerary for you – and if we don't have one, we'll tailor-make one! From the main sights to remote villages, our locally based Travel Specialists will give you unique insights into every place you visit and let you delve into known destinations from new perspectives.

Our tours offer a variety of hotel and resort options, premium stays in deluxe accommodation, heritage hotels, a five-star boutique or on the water in a junk. Tap into our experience let us create an experience unique to you – and one you will never forget.

What type of Holiday to Asia?

Our itineraries at Lantern Route are created according to different inspirations. Some travelers are interested in the History & Culture of a destination, while some like to stay active with Adventure tours. A Cross Border trip explores different countries in a single tour, while Ultimate Luxury tours offer the highest level of exclusivity across our destinations. There are 14 different Holiday Types to choose from, or you can mix and match ideas to create your dream vacation.

Target Market(s)

Slightly more female, aged 30-65, are creative, professional and looking for something different, something a bit unusual.

Industry/Entity Type

Boutique

Requirements
Must have
• 5 page designs:

1. Homepage
2. Tours list page for a country
3. Tour page
4. 'Be Inspired' page
5. Country page
6. Enquiry page

Our inspirations.

The following list shows websites we love and which inspire us... to give you some indication of our preferred styles, functions and layouts:

http://www.frostvale.com/en/ (we really like this, great personality, like the use of icons for tour types)
http://www.pebbletrek.co.uk/ (very simple design elements and layout)
http://www.sunmarrow.com/ (great use of background image, nice simple nav bar)
http://www.roamkestrel.org/ (we like because it has distinct personality and is well suited to the destination)
http://www.seebrantown.com/ (clear personality through font use)
http://www.vastquarry.com/ (original, unique)
http://www.ploverjournal.com/grand-tour-of-asia (like the map style)

Key design points:

1. You must use our existing logo (attached), but you can change the color scheme of the logo to accord with the whichever color scheme you choose for the main designs.
2. Our logo strapline is "Asia is our Lantern" and should be used prominently on the page to reinforce the meaning of our company name.
3. Home page and tours list pages should allow the user to see the choice of tours immediately without scrolling & Introduction copy should be minimal.
4. We and our site visitors are inspired and excited by our photography, this is an element of the site which we would like to maintain and build on, though the section page header sliders are currently too big and do not allow quick access to the section content. This is a design problem which needs a solution. Full page photographic backgrounds may be an answer?
5. Tour page should display other contextual tours, from the same country or style/type
6. We should promote press coverage in various places
7. We should display consultant profiles in various places
8. Map designs for tour page and country page, plus a modal pop out for the home page. These are complex and may have a few small photos and short descriptive text only, though this is limited by your own creativity. We will use graphics and html5/css3 so there are no creative limitations.
9. The 'Inspirations' / 'Be Inspired' page is for people who want travel and holiday ideas, who are looking for inspiration on where to go and what to do. This section needs to reflect the exotic, the unusual, the extraordinary in our destinations and tours, and we leave this to your creative genius to develop. We are also interested in how this inspirations page is related to the blog and social media content we produce daily, is there an integration here? Can we present YouTube videos, our blog posts, Facebook posts etc, on this page? This is another design challenge.
10. We would like to see designs for the tours list page which feature AJAX content filtering (for instance: http://demo.skinmorrow.com/?acn), we would like to see how to include this type of content filtering on homepage and destination page also.
11. The 'Enquiry' call to action should be on all pages and prominent.
12. The enquiry page can reflect the same fields as the existing website enquiry page

Values to be communicated:

- Exotic: Asia is exotic, and our tours will expose clients to extraordinary sights and unusual cultural encounters.
- Authentic: Our travel consultants all live in the destinations themselves, they are local nationals and have all the insider knowledge to give clients a truly authentic experience of our destinations
- Unique: All of our tours are tailor made, there are no fixed departure dates or join-in groups. All tour itineraries can be uniquely designed for our clients, from departure dates to destinations.
- Trust: Some travelers prefer to book their holidays with local agencies they can meet in person, rather than with online companies like us who live in the destinations and who they only get to meet on Skype video or phone. We want to convey that we are trustworthy. We have attempted this through presenting a 'meet the team' page and a 'press' page and advert, as well as offering a prominent international phone number. How we you build on this and further convey this value?

```html
<!DOCTYPE html>
<html lang="en">
<head>
<meta charset="utf-8">
<title>Lantern Route – Asia is our Lantern</title>
<link href="https://fonts.googleapis.com/css2?family=Fira+Sans:wght@300;400&family=Oswald:wght@300;400&family=Arimo:wght@400&display=swap" rel="stylesheet">
<style>
:root{
  --header:#3a3a3a;
  --header-top:#444;
  --nav:#1f1f1f;
  --panel:#3c3c3c;
  --field:#333;
  --footer:#3b3b3b;
  --footer-bottom:#2d2d2d;
  --accent-teal:#9cbfc2;
  --heading-teal:#9bb6b9;
  --map:#bfd5d5;
  --orange-dark:#d27408;
  --chat:#f5a76c;
  --body-text:#4a4a4a;
  --white:#fff;
}
*{box-sizing:border-box;margin:0;padding:0}
html,body{width:1200px;height:1174px;overflow:hidden}
body{font-family:"Fira Sans",sans-serif;background:var(--white);position:relative;color:var(--body-text)}
a{color:inherit;text-decoration:none}
ul{list-style:none}

/* header */
.site-header{position:absolute;left:0;top:0;width:1200px;height:70px;background:linear-gradient(var(--header-top),var(--header))}
.brand-mark{position:absolute;left:126px;top:10px;width:58px;height:48px;border-radius:6px;background:#a9c8ca}
.brand-name{position:absolute;left:201px;top:17px;font-size:24px;color:var(--white);letter-spacing:-.6px;line-height:28px;white-space:nowrap}
.brand-tag{position:absolute;left:260px;top:42px;font-size:11px;line-height:13px;color:#cfcfcf;white-space:nowrap}
.header-btn{position:absolute;top:24px;height:32px;background:#2e2e2e;border:1px solid #222;border-radius:2px;color:#ddd;font-family:"Arimo",sans-serif;font-size:10px;display:flex;align-items:center;gap:6px;padding:0 10px;text-transform:uppercase;white-space:nowrap}
.login{left:543px;width:124px;padding-left:13px}
.cart{left:678px;width:167px;padding-right:0}
.cart-total{margin-left:auto;height:30px;width:56px;background:#3d3d3d;display:flex;align-items:center;padding-left:9px}
.cart-count{position:absolute;left:-4px;top:-4px;width:15px;height:15px;border-radius:50%;background:#555;font-size:8px;display:flex;align-items:center;justify-content:center;color:#ddd}
.search{position:absolute;left:853px;top:24px;width:230px;height:32px;background:#555;border:1px solid #3a3a3a;border-radius:2px;font-family:"Arimo",sans-serif;font-size:10px;color:#bbb;padding:9px 11px}
.search svg{position:absolute;right:12px;top:8px}

/* nav */
.main-nav{position:absolute;left:0;top:70px;width:1200px;height:37px;background:var(--nav);border-top:1px solid #111}
.main-nav ul{display:flex;position:absolute;left:114px;top:0;height:36px}
.main-nav li{font-family:"Oswald",sans-serif;font-size:14px;color:#f2f2f2;padding:0 15px;line-height:36px;border-left:1px solid #333;letter-spacing:-.3px;white-space:nowrap}
.main-nav li:first-child{border-left:0;color:var(--accent-teal)}

/* hero */
.hero{position:absolute;left:0;top:107px;width:1200px;height:423px;background:radial-gradient(ellipse at 62% 8%,#fff3d8 0,#e7a866 14%,transparent 34%),linear-gradient(110deg,#6a3a1d 0%,#a8643a 28%,#7a4526 50%,#c37d48 70%,#5c3218 100%)}
.finder{position:absolute;left:789px;top:120px;width:294px;height:390px;background:var(--panel);box-shadow:0 0 4px rgba(0,0,0,.4)}
.finder-tabs{display:flex;height:45px}
.finder-tab{font-family:"Oswald",sans-serif;font-size:22px;color:var(--white);display:flex;align-items:center;justify-content:center}
.finder-tab.active{width:133px;background:#3c3c3c;border-right:1px solid #2c2c2c}
.finder-tab:last-child{flex:1;background:#454545}
.field{position:absolute;left:22px;width:249px;height:36px;background:var(--field);border-bottom:1px solid #555;font-family:"Arimo",sans-serif;font-size:14px;color:#c8c8c8;padding:10px 13px}
.field svg{position:absolute;right:8px;top:11px}
.range-labels{position:absolute;left:23px;top:273px;width:252px;display:flex;justify-content:space-between;font-family:"Arimo",sans-serif;font-size:12px;color:#ccc}
.range-track{position:absolute;left:23px;top:297px;width:252px;height:4px;background:#222;border-radius:2px}
.range-fill{position:absolute;left:4px;width:143px;height:4px;background:var(--accent-teal)}
.range-knob{position:absolute;top:-4px;width:8px;height:12px;background:#2a2a2a;border:1px solid #555}
.search-btn{position:absolute;left:82px;top:323px;width:130px;height:46px;background:linear-gradient(#f69a25,var(--orange-dark));border:1px solid #b8650a;border-radius:2px;font-family:"Oswald",sans-serif;font-size:19px;color:var(--white);display:flex;align-items:center;justify-content:center}

/* intro */
.intro{position:absolute;left:0;top:530px;width:1200px;height:273px;border-top:2px solid #cfe0e0}
.intro-map{position:absolute;left:118px;top:14px;width:275px;height:228px;background:radial-gradient(ellipse at 45% 40%,var(--map) 0,#d4e3e3 55%,#fff 78%)}
.intro-copy{position:absolute;left:442px;top:34px;width:640px}
.intro-copy h1{font-size:28px;font-weight:400;color:var(--heading-teal);line-height:30px;margin-bottom:11px}
.intro-copy p{font-size:14px;line-height:18.3px;margin-bottom:18px}

/* footer */
.site-footer{position:absolute;left:0;top:803px;width:1200px;height:324px;background:var(--footer);border-top:2px solid #b7cdcd}
.footer-col{position:absolute;top:38px}
.footer-col h2{font-weight:300;font-size:15px;line-height:18px;color:#cfcfcf;letter-spacing:.4px;margin-bottom:6px;white-space:nowrap}
.footer-col li{font-size:13px;color:#c9c9c9;line-height:26.7px;white-space:nowrap}
.col-about li{line-height:24px}
.contact-line{display:flex;align-items:center;gap:12px;font-size:13px;color:#cfcfcf;margin-bottom:12px;white-space:nowrap}
.social{display:flex;gap:7px;margin-top:10px}
.social span{width:26px;height:26px;background:#464646;border:1px solid #333}
.newsletter{position:absolute;left:850px;top:42px;width:233px}
.newsletter p{font-size:13px;color:#cfcfcf;line-height:17px}
.subscribe{display:flex;margin-top:16px;height:38px}
.subscribe-field{flex:1;background:#2f2f2f;border:1px solid #555;font-family:"Arimo",sans-serif;font-size:14px;color:#ddd;padding:10px}
.subscribe-btn{width:49px;background:linear-gradient(#f69a25,var(--orange-dark));font-family:"Oswald",sans-serif;font-size:20px;color:var(--white);display:flex;align-items:center;justify-content:center}
.footer-bottom{position:absolute;left:0;top:1127px;width:1200px;height:47px;background:var(--footer-bottom);font-size:10px;color:#999;padding:18px 117px}

/* enquiry chat */
.chat-bubble{position:absolute;left:958px;top:1062px;width:238px;height:67px;background:var(--chat);border:2px solid #fff0e0;border-radius:16px;box-shadow:0 0 3px rgba(0,0,0,.3)}
.chat-tail{position:absolute;left:976px;top:1126px}
.chat-title{position:absolute;left:20px;top:7px;font-size:21px;color:#3b3b3b}
.chat-sub{position:absolute;left:49px;top:36px;font-family:"Arimo",sans-serif;font-size:11px;color:#333;white-space:nowrap}
.chat-close{position:absolute;right:16px;top:8px;font-family:"Arimo",sans-serif;font-size:13px;color:#333}
.chat-bar{position:absolute;left:936px;top:1142px;width:258px;height:32px;background:#393939;border:1px solid #666;border-bottom:0;display:flex;align-items:center;padding-left:34px;font-family:"Arimo",sans-serif;font-size:15px;color:#ddd;gap:10px;white-space:nowrap}
.status-dot{width:15px;height:15px;border-radius:50%;background:#5bb52c}
.status-online{color:#7ccb3a}
</style>
</head>
<body>

<header class="site-header">
  <span class="brand-mark"></span>
  <a class="brand-name" href="#">Lantern Route</a>
  <span class="brand-tag">Asia is our lantern.</span>
  <a class="header-btn login" href="#">
    <svg width="12" height="12" viewBox="0 0 12 12"><circle cx="6" cy="3.5" r="3" fill="#ddd"/><path d="M0 12c0-4 3-5 6-5s6 1 6 5z" fill="#ddd"/></svg>
    Login / Register
  </a>
  <a class="header-btn cart" href="#">
    <span class="cart-count">0</span>
    <svg width="14" height="11" viewBox="0 0 14 11"><path d="M0 1h2.5l2 6h7l2-5H4" fill="none" stroke="#ddd" stroke-width="1.3"/><circle cx="5.5" cy="9.5" r="1.2" fill="#ddd"/><circle cx="10.5" cy="9.5" r="1.2" fill="#ddd"/></svg>
    Shopping Cart
    <span class="cart-total">$0.00</span>
  </a>
  <div class="search">Search...
    <svg width="14" height="14" viewBox="0 0 14 14"><circle cx="5.5" cy="5.5" r="4.3" fill="none" stroke="#fff" stroke-width="2"/><path d="M8.6 8.6l4.3 4.3" stroke="#fff" stroke-width="2.4"/></svg>
  </div>
</header>

<nav class="main-nav">
  <ul>
    <li>HOME</li><li>DESTINATIONS</li><li>TOURS</li><li>HOLIDAY TYPES</li><li>BEST VALUE</li><li>ABOUT US</li><li>BLOG</li>
  </ul>
</nav>

<section class="hero" role="img" aria-label="Photograph of travellers walking down the steps of an ancient carved stone temple in warm sunlight"></section>

<form class="finder">
  <div class="finder-tabs"><div class="finder-tab active">TOURS</div><div class="finder-tab">HOTELS</div></div>
  <div class="field" style="top:63px">Country<svg width="12" height="8" viewBox="0 0 12 8"><path d="M1 1l5 5 5-5" fill="none" stroke="#666" stroke-width="1.6"/></svg></div>
  <div class="field" style="top:116px">City<svg width="12" height="8" viewBox="0 0 12 8"><path d="M1 1l5 5 5-5" fill="none" stroke="#666" stroke-width="1.6"/></svg></div>
  <div class="field" style="top:169px">Departure Date<svg width="16" height="14" viewBox="0 0 16 14"><rect width="16" height="14" fill="#aaa"/><rect width="16" height="3" fill="#ddd"/></svg></div>
  <div class="field" style="top:221px">Arrival Date<svg width="16" height="14" viewBox="0 0 16 14"><rect width="16" height="14" fill="#aaa"/><rect width="16" height="3" fill="#ddd"/></svg></div>
  <div class="range-labels"><span>$259</span><span>$2.289</span></div>
  <div class="range-track"><div class="range-fill"></div><span class="range-knob" style="left:-1px"></span><span class="range-knob" style="left:133px"></span></div>
  <div class="search-btn">Search Tours</div>
</form>

<section class="intro">
  <div class="intro-map" role="img" aria-label="Pale map of Asia"></div>
  <div class="intro-copy">
    <h1>ASIA IS OUR LANTERN</h1>
    <p>No one knows a destination better than someone who lives, works and plays there. That's the foundation of Lantern Route. Our travel specialists reside in Asia. They live Asia, they breathe Asia. And they're intrigued explorers as much as they are citizens of Bangkok, or Bali, or Luang Prabang.</p>
    <p>The result is a travel company tailor-made for the person with a taste for veering off the well-trodden path, for the adventurer who wants access to Asia's most spectacular sights, but hidden charms as well, on the road less traveled.</p>
    <p>Want to explore this Asia? Step into our Lantern.</p>
  </div>
</section>

<footer class="site-footer">
  <div class="footer-col" style="left:117px">
    <h2>QUICK LINKS</h2>
    <ul><li>Home</li><li>Destinations</li><li>Tours</li><li>Holiday types</li><li>Best Value</li><li>About Us</li><li>Blog</li></ul>
  </div>
  <div class="footer-col" style="left:250px">
    <h2>OUR LANTERN</h2>
    <ul><li>Thailand</li><li>Indonesia</li><li>Laos</li><li>Cambodia</li><li>Japan</li><li>Myanmar</li><li>Vietnam</li><li>China</li><li>Multi-country</li></ul>
  </div>
  <div class="footer-col col-about" style="left:389px">
    <h2>ABOUT LANTERN ROUTE</h2>
    <ul><li>Why book with us</li><li>About us</li><li>Meet the team</li><li>Careers</li><li>In the press</li><li>Affiliate Program</li></ul>
  </div>
  <div class="footer-col" style="left:609px">
    <h2>CONTACTS</h2>
    <div class="contact-line" style="margin-top:14px">
      <svg width="14" height="18" viewBox="0 0 14 18"><path d="M3 1l3 4-2 2c1 3 3 5 5 6l2-2 3 3-3 3C6 16 1 10 1 3z" fill="#bbb"/></svg>
      +1 (001) 555-41-26
    </div>
    <div class="contact-line">
      <svg width="14" height="10" viewBox="0 0 14 10"><rect width="14" height="10" fill="#bbb"/><path d="M0 0l7 6 7-6" fill="none" stroke="#3b3b3b" stroke-width="1.2"/></svg>
      info@lanternroute.com
    </div>
    <div class="social"><span></span><span></span><span></span><span></span><span></span><span></span></div>
  </div>
  <div class="newsletter">
    <p>Sign up to our Newsletter and receive occasional e-mail updates about new features and special offers from our company.</p>
    <div class="subscribe"><div class="subscribe-field">Email address</div><div class="subscribe-btn">GO!</div></div>
  </div>
</footer>

<div class="footer-bottom">Copyright © 2013 Lantern Route.&nbsp; All Rights Reserved.</div>

<div class="chat-bubble">
  <span class="chat-title">Question?</span>
  <span class="chat-close">x</span>
  <span class="chat-sub">Click here to ask one of our experts</span>
</div>
<svg class="chat-tail" width="30" height="16" viewBox="0 0 30 16"><path d="M2 0v15L22 0z" fill="#f5a76c" stroke="#fff0e0" stroke-width="2"/><path d="M3 0h18" stroke="#f5a76c" stroke-width="3"/></svg>
<div class="chat-bar"><span class="status-dot"></span><span><span class="status-online">Online</span> - Leave a message</span></div>

</body>
</html>
```